Flyer Design

I'm looking for a new flyer design to help promote our landscape company, and some of our main service for the up and coming season. We're trying to position ourselves as a leader in our market, so obviously quality is important to us.

Our current promotion is 25% off the first month with signup of annual service.

Phone Number: (816) 555-0193
Website: gardelvista.com
Our tagline: "Your hands are full... Let us help"

The call to action: direct them to our website for a detailed list of services and to receive a free quote.

You're welcome to add your own wording and punctuation. If I like the design I will provide feedback accordingly.

I have attached a jpg of our logo to help with design colors. I will provide the vector file upon completion of this project.

Also, I've attached a few photos that I had on hand of our companies work that may help with the design. Obviously I don't want to use them all, but there are a couple just to help out. I'm not opposed to stock photos either.
Thanks

Target Market(s)

We market to high end customers, generally with home between $500k-$2mil, or household income over $200k. Quality and creativity are most important to us.

Industry/Entity Type

Landscape

Requirements
Must have
• Creativity, easy to read, modern style.

```html
<!DOCTYPE html>
<html lang="en">
<head>
<meta charset="utf-8">
<title>Gardel Vista – Lawn Service Flyer</title>
<link href="https://fonts.googleapis.com/css2?family=Alegreya:ital,wght@1,800;1,900&display=swap" rel="stylesheet">
<style>
  :root {
    --orange: #e0593a;
    --dark: #3b3a2e;
    --cream: #f3eedb;
    --house: #8a7a6c;
    --shrub: #3a4f30;
    --lawn: #55803a;
    --ground: #cfc9bc;
  }
  * { margin: 0; padding: 0; box-sizing: border-box; }
  html, body { width: 1200px; height: 923px; overflow: hidden; background: #fff; }
  body { font-family: "Alegreya", Georgia, serif; font-style: italic; font-weight: 900; }

  .flyer { position: relative; width: 1200px; height: 923px; overflow: hidden; }

  .scene-photo {
    position: absolute; inset: 0;
    background: linear-gradient(180deg,
      var(--house) 0%,
      #7c7063 22%,
      var(--shrub) 38%,
      var(--lawn) 55%,
      var(--lawn) 84%,
      var(--ground) 97%);
  }

  .brand {
    position: absolute; left: 31px; top: 33px;
    display: flex; align-items: center; gap: 14px;
  }
  .brand-dot { width: 46px; height: 46px; border-radius: 50%; background: var(--orange); }
  .brand-name { color: var(--cream); font-size: 34px; letter-spacing: .5px; }

  .promo { position: absolute; left: 678px; top: 31px; width: 492px; }
  .promo-headline {
    height: 98px; background: var(--orange); color: var(--cream);
    font-size: 36px; letter-spacing: .5px;
    display: flex; align-items: center; justify-content: center;
  }
  .promo-detail {
    height: 69px; background: var(--cream); color: var(--dark);
    font-size: 21px; letter-spacing: .3px;
    display: flex; align-items: center; justify-content: center;
  }

  .services { position: absolute; top: 338px; left: 0; width: 1200px; }
  .service { position: absolute; width: 150px; text-align: center; }
  .service:nth-child(1) { left: 138px; }
  .service:nth-child(2) { left: 396px; }
  .service:nth-child(3) { left: 654px; }
  .service:nth-child(4) { left: 912px; }
  .service-icon {
    width: 150px; height: 150px; border-radius: 50%; background: var(--orange);
    display: flex; align-items: center; justify-content: center;
  }
  .service-icon svg { width: 96px; height: 96px; }
  .service-label {
    margin-top: 22px; height: 52px; background: var(--dark); color: var(--cream);
    font-size: 32px; line-height: 50px; letter-spacing: .5px;
  }
  .service-label-foot { height: 18px; background: var(--cream); }

  .footer { position: absolute; left: 0; top: 784px; width: 1200px; height: 109px; display: flex; }
  .tagline {
    width: 734px; background: var(--dark); color: var(--cream);
    font-size: 35px; letter-spacing: .4px;
    display: flex; align-items: center; padding-left: 71px;
  }
  .contact {
    flex: 1; background: var(--orange); color: var(--cream);
    font-size: 35px; line-height: 42px; letter-spacing: .5px;
    display: flex; flex-direction: column; align-items: center; justify-content: center;
  }
</style>
</head>
<body>
<main class="flyer">
  <div class="scene-photo" role="img" aria-label="Photo of a freshly striped green front lawn with shrubs and a curved driveway before a large home"></div>

  <div class="brand">
    <span class="brand-dot"></span>
    <span class="brand-name">Gardel Vista</span>
  </div>

  <section class="promo">
    <div class="promo-headline">25% off the first month</div>
    <div class="promo-detail">when you sign up for weekly lawn service</div>
  </section>

  <section class="services">
    <div class="service">
      <div class="service-icon">
        <svg viewBox="0 0 96 96" fill="none" stroke="#3b3a2e" stroke-width="5" stroke-linecap="round">
          <path d="M20 52 h56 a12 12 0 0 0 -6 -22 a18 18 0 0 0 -34 -2 a12 12 0 0 0 -16 24z" fill="#3b3a2e" stroke="none"/>
          <path d="M28 66 v16 M20 74 h16 M22 68 l12 12 M34 68 l-12 12"/>
          <path d="M60 66 v16 M52 74 h16 M54 68 l12 12 M66 68 l-12 12"/>
        </svg>
      </div>
      <div class="service-label">snow</div>
      <div class="service-label-foot"></div>
    </div>
    <div class="service">
      <div class="service-icon">
        <svg viewBox="0 0 96 96" fill="#3b3a2e">
          <rect x="14" y="10" width="6" height="48" rx="3" transform="rotate(-30 17 34)"/>
          <path d="M30 52 h52 v14 h-52z"/>
          <circle cx="34" cy="72" r="9"/>
          <circle cx="76" cy="72" r="9"/>
        </svg>
      </div>
      <div class="service-label">mowing</div>
      <div class="service-label-foot"></div>
    </div>
    <div class="service">
      <div class="service-icon">
        <svg viewBox="0 0 96 96" fill="none" stroke="#3b3a2e" stroke-width="5" stroke-linejoin="round">
          <path d="M28 60 a16 16 0 0 1 -4 -30 a22 22 0 0 1 44 -2 a16 16 0 0 1 2 32z"/>
          <path d="M44 88 v-30 l-10 -10 M52 88 v-24 l10 -12"/>
        </svg>
      </div>
      <div class="service-label">tree</div>
      <div class="service-label-foot"></div>
    </div>
    <div class="service">
      <div class="service-icon">
        <svg viewBox="0 0 96 96" fill="#3b3a2e">
          <circle cx="30" cy="16" r="6"/><circle cx="48" cy="16" r="6"/><circle cx="66" cy="16" r="6"/>
          <circle cx="30" cy="32" r="4"/><circle cx="48" cy="32" r="4"/><circle cx="66" cy="32" r="4"/>
          <circle cx="30" cy="44" r="3"/><circle cx="48" cy="44" r="3"/><circle cx="66" cy="44" r="3"/>
          <rect x="18" y="60" width="60" height="20" rx="6"/>
        </svg>
      </div>
      <div class="service-label">Aeration</div>
      <div class="service-label-foot"></div>
    </div>
  </section>

  <footer class="footer">
    <div class="tagline">Your hands are full... Let us help</div>
    <div class="contact">
      <span class="contact-phone">(816) 555-0193</span>
      <span class="contact-web">gardelvista.com</span>
    </div>
  </footer>
</main>
</body>
</html>
```